Quorvel Landing page redesign

We are looking for a landing page redesign before we officially launch. We want to incorporate the information already on the site at www.Quorvel-example.com landing page but make it more inviting. There needs to be a sign up section along with clearly stating what we do. Having a place for sample profiles and linking to our blog and podcast is option. More information about all we will be doing is at Quorvel is on the landing page and also on the blog.

Target Market(s)

35 years old and up.

Coding

Coded - Design and coding required

Number of Pages Required

1 page

Requirements
Must have
• The top bar and the bottom bar (with the privacy policy, etc)
• Sign in/up section.
• I don't want to give to much here because I want designers to be creative.
Nice to have
• Prefer not to have a landing page that requires a lot of scrolling at all.

```html
<!DOCTYPE html>
<html lang="en">
<head>
<meta charset="UTF-8">
<title>Quorvel Pages</title>
<link rel="stylesheet" href="https://fonts.googleapis.com/css2?family=Raleway:wght@400;500;600;700&display=swap">
<style>
  :root {
    --navy-deep: #0b1450;
    --navy-mid: #1a2a8a;
    --navy-button: #121c3e;
    --orange: #f5a00b;
    --white: #ffffff;
    --ink: #1e2233;
    --ink-soft: #333845;
    --arrow-grey: #4a4d5a;
    --input-border: #9aa0ad;
  }
  * { box-sizing: border-box; margin: 0; padding: 0; }
  html, body { width: 1200px; height: 645px; overflow: hidden; background: var(--white); }
  body { font-family: "Raleway", Arial, sans-serif; color: var(--ink); position: relative; }

  .hero {
    position: absolute; left: 0; top: 0; width: 1200px; height: 386px;
    background: radial-gradient(ellipse at 60% 40%, var(--navy-mid) 0%, var(--navy-deep) 70%);
  }

  .brand { position: absolute; color: var(--white); font-weight: 500; }
  .brand--header { left: 99px; top: 24px; font-size: 23px; }
  .brand--footer { left: 99px; top: 585px; font-size: 19px; color: var(--ink); }

  .main-nav { position: absolute; top: 27px; left: 897px; display: flex; }
  .main-nav a { color: var(--white); text-decoration: none; font-size: 15.5px; font-weight: 500; }
  .main-nav a:nth-child(1) { margin-right: 28px; }
  .main-nav a:nth-child(2) { margin-right: 34px; }

  .hero-title {
    position: absolute; left: 98px; top: 112px;
    font-size: 41px; font-weight: 400; color: var(--white); letter-spacing: 0.3px;
  }
  .feature-list { position: absolute; left: 101px; top: 175px; list-style: none; }
  .feature-list li {
    display: flex; align-items: center; color: var(--white);
    font-size: 15.5px; height: 28.3px; font-weight: 400;
  }
  .feature-list li svg { width: 14px; height: 12px; margin-right: 6px; flex: none; }
  .feature-list strong { font-weight: 700; margin-right: 4px; }

  .intro {
    position: absolute; left: 101px; top: 409px; width: 455px;
    font-size: 14.6px; line-height: 26px; color: var(--ink-soft);
  }
  .sample-links { position: absolute; left: 99px; top: 484px; display: flex; gap: 9px; }
  .sample-links a {
    display: flex; align-items: center; justify-content: center;
    height: 47px; width: 218px; border-radius: 3px;
    font-size: 15.5px; font-weight: 700; color: var(--white); text-decoration: none;
  }
  .btn-profile { background: var(--navy-button); }
  .btn-legacy { background: var(--orange); }

  .signup-panel {
    position: absolute; left: 613px; top: 81px; width: 488px; height: 305px;
    background: var(--white);
  }
  .signup-title {
    position: absolute; left: 613px; top: 101px; width: 488px; text-align: center;
    font-size: 29px; font-weight: 400; color: var(--ink);
  }
  .preview-shot {
    position: absolute; left: 661px; top: 164px; width: 391px; height: 262px;
    background: linear-gradient(180deg, #1f2a6e 0 8%, #fbf7d6 8% 66%, #d9d9d9 66% 100%);
    box-shadow: 0 2px 4px rgba(0,0,0,0.3);
    border: 3px solid var(--white);
  }
  .carousel-arrow {
    position: absolute; top: 281px; width: 26px; height: 26px;
    background: var(--arrow-grey); display: flex; align-items: center; justify-content: center;
  }
  .carousel-arrow--prev { left: 633px; }
  .carousel-arrow--next { left: 1056px; }

  .subscribe-form { position: absolute; left: 633px; top: 456px; display: flex; }
  .email-field {
    width: 319px; height: 47px; border: 1px solid var(--input-border); border-right: none;
    border-radius: 3px 0 0 3px; padding: 0 14px; display: flex; align-items: center;
    font-size: 15.5px; color: var(--ink-soft); font-family: inherit;
  }
  .subscribe-btn {
    width: 126px; height: 47px; background: var(--navy-button); color: var(--white);
    border: none; border-radius: 0 3px 3px 0; font-family: inherit; font-size: 15.5px; font-weight: 700;
  }
  .signin-note { position: absolute; left: 636px; top: 514px; font-size: 12px; color: var(--ink); }
  .signin-note a { color: var(--ink); font-weight: 700; text-decoration: none; }

  .footer-links {
    position: absolute; right: 101px; top: 591px; display: flex; gap: 5px;
    font-size: 10.5px; color: var(--ink-soft);
  }
  .footer-links a { color: var(--ink-soft); text-decoration: none; }
</style>
</head>
<body>
  <header>
    <div class="hero" role="img" aria-label="Dark blue tinted photo of hands working on a laptop"></div>
    <div class="brand brand--header">Quorvel</div>
    <nav class="main-nav">
      <a href="#">Blog</a>
      <a href="#">Podcast</a>
      <a href="#">Login</a>
    </nav>
  </header>

  <main>
    <h1 class="hero-title">QUORVEL PAGES</h1>
    <ul class="feature-list">
      <li><svg viewBox="0 0 14 12"><path d="M1 6.5 5 10.5 13 1.5" fill="none" stroke="#fff" stroke-width="2.6"/></svg><strong>Create</strong> Timelines, Maps, Family Trees</li>
      <li><svg viewBox="0 0 14 12"><path d="M1 6.5 5 10.5 13 1.5" fill="none" stroke="#fff" stroke-width="2.6"/></svg><strong>Memorialize</strong> Loved Ones</li>
      <li><svg viewBox="0 0 14 12"><path d="M1 6.5 5 10.5 13 1.5" fill="none" stroke="#fff" stroke-width="2.6"/></svg><strong>Share</strong> Family Stories, History and more</li>
      <li><svg viewBox="0 0 14 12"><path d="M1 6.5 5 10.5 13 1.5" fill="none" stroke="#fff" stroke-width="2.6"/></svg><strong>Control</strong> Your Privacy</li>
      <li><svg viewBox="0 0 14 12"><path d="M1 6.5 5 10.5 13 1.5" fill="none" stroke="#fff" stroke-width="2.6"/></svg><strong>No</strong> Ads, No Like Buttons</li>
      <li><svg viewBox="0 0 14 12"><path d="M1 6.5 5 10.5 13 1.5" fill="none" stroke="#fff" stroke-width="2.6"/></svg><strong>No</strong> News Feeds</li>
    </ul>

    <p class="intro">Build multiple Quorvel pages through one account for yourself, your family and to keep loved one's legacies alive.</p>
    <div class="sample-links">
      <a class="btn-profile" href="#">Sample Quorvel Profile</a>
      <a class="btn-legacy" href="#">Sample Legacy Profile</a>
    </div>

    <section class="signup">
      <div class="signup-panel"></div>
      <h2 class="signup-title">Become an Early User</h2>
      <div class="preview-shot" role="img" aria-label="App screen showing a child's five year check-up entry with growth chart fields and a media strip of family photos"></div>
      <span class="carousel-arrow carousel-arrow--prev"><svg width="10" height="12" viewBox="0 0 10 12"><path d="M8 1 3 6l5 5" fill="none" stroke="#fff" stroke-width="2.5"/></svg></span>
      <span class="carousel-arrow carousel-arrow--next"><svg width="10" height="12" viewBox="0 0 10 12"><path d="M2 1l5 5-5 5" fill="none" stroke="#fff" stroke-width="2.5"/></svg></span>
      <form class="subscribe-form">
        <span class="email-field">Enter Your Email Address</span>
        <button class="subscribe-btn" type="button">Subscribe</button>
      </form>
      <p class="signin-note">Already Have an Account? <a href="#">Sign in</a></p>
    </section>
  </main>

  <footer>
    <div class="brand brand--footer">Quorvel</div>
    <nav class="footer-links">
      <a href="#">Privacy Policy</a>
      <a href="#">Terms of Use</a>
      <a href="#">Data Tracking Policy</a>
      <a href="#">Submit Feedback</a>
      <span>Quorvel © 2017</span>
    </nav>
  </footer>
</body>
</html>
```